Solar Advertising Flier to generate Biz

I need a advertisement that generates business to be used in a mailer for marketing purposes.

Im attaching a file that is a an idea of advertisement.
I do not want the "ZVN" specific information on it.
I want the background solar panels.
Same information as the ad.
And I've attached my Logo - I want the color scheme to match this.

Thank you

Target Market(s)

Middle to Upper Class Home Owners

Industry/Entity Type

Solar Energy

Requirements
Must have
• A call to action
• A professional look
Nice to have
• A family
• Great looking solar panels
Should not have
• Cartoons

```html
<!DOCTYPE html>
<html lang="en">
<head>
<meta charset="utf-8">
<title>Go Solar – Bright Roof Energy Flier</title>
<link rel="stylesheet" href="https://fonts.googleapis.com/css2?family=Lato:wght@400;700;900&family=Fira+Sans+Extra+Condensed:wght@500;600&display=swap">
<style>
  :root {
    --blue: #1b93d2;
    --blue-deep: #0f6fa8;
    --green: #8cc63f;
    --green-light: #c4df4c;
    --ink: #1a1a1a;
    --white: #ffffff;
    --stage: #eeeeee;
  }
  * { box-sizing: border-box; margin: 0; padding: 0; }
  html, body { width: 1200px; height: 1200px; overflow: hidden; background: var(--stage); }
  .flier {
    position: absolute; left: 190px; top: 20px;
    width: 900px; height: 1273px;
    transform: scale(0.9112); transform-origin: top left;
    background: var(--white); overflow: hidden;
    font-family: "Lato", sans-serif; color: var(--ink);
  }
  .flier-shapes { position: absolute; inset: 0; }
  .headline {
    position: absolute; left: 40px; top: 52px; width: 340px;
    text-align: center; color: var(--blue); font-weight: 900;
    font-size: 100px; line-height: 110px; letter-spacing: -1px;
  }
  .easy-ribbon {
    position: absolute; left: 150px; top: 380px; width: 313px; height: 42px;
    color: var(--white); font-weight: 900; font-size: 28px; line-height: 42px;
    padding-left: 12px;
  }
  .benefits { position: absolute; left: 55px; top: 448px; width: 370px; list-style: none; }
  .benefits li {
    position: relative; padding-left: 30px; font-size: 24px; line-height: 31px;
    margin-bottom: 21px; color: #222;
  }
  .benefits li::before {
    content: ""; position: absolute; left: 2px; top: 8px; width: 15px; height: 15px;
    border: 2px solid #222; border-radius: 50%;
  }
  .benefits b { font-weight: 900; }
  .brand {
    position: absolute; left: 560px; top: 690px; width: 250px; text-align: center;
  }
  .brand-dot {
    display: block; margin: 0 auto 14px; width: 96px; height: 96px;
    border: 6px solid var(--green); border-radius: 50%;
  }
  .brand-name { color: var(--blue); font-weight: 700; font-size: 30px; line-height: 34px; letter-spacing: 1px; }
  .how-title {
    position: absolute; left: 45px; top: 815px; color: var(--blue);
    font-weight: 900; font-size: 29px; letter-spacing: -0.5px;
  }
  .how-text {
    position: absolute; left: 45px; top: 858px; width: 800px;
    font-size: 24.5px; line-height: 36.5px; text-align: justify; color: #222;
  }
  .how-text b { font-weight: 900; }
  .contact { position: absolute; left: 43px; top: 1098px; color: var(--white); }
  .contact-lead { font-family: "Fira Sans Extra Condensed", sans-serif; font-weight: 600; font-size: 30px; letter-spacing: 0.5px; }
  .contact-phone { font-family: "Fira Sans Extra Condensed", sans-serif; font-weight: 600; font-size: 54px; line-height: 62px; letter-spacing: 1px; }
  .contact-web { font-size: 28px; font-weight: 700; line-height: 34px; }
  .rebate {
    position: absolute; left: 630px; top: 1038px; width: 260px; text-align: center;
    text-transform: uppercase; font-weight: 900; letter-spacing: -0.5px;
  }
  .rebate-call { color: var(--blue); font-size: 32px; line-height: 32px; font-weight: 700; }
  .rebate-receive { font-size: 30px; line-height: 32px; }
  .rebate-amount { color: var(--green); font-size: 84px; line-height: 82px; letter-spacing: -3px; }
  .rebate-label { font-size: 30px; line-height: 30px; }
  .rebate-terms { font-size: 6.5px; line-height: 9px; font-weight: 400; text-transform: none; letter-spacing: 0; margin-top: 3px; }
</style>
</head>
<body>
<main class="flier">
  <svg class="flier-shapes" viewBox="0 0 900 1273" width="900" height="1273">
    <defs>
      <clipPath id="family-clip"><circle cx="700" cy="215" r="292"/></clipPath>
      <clipPath id="installer-clip"><circle cx="675" cy="500" r="156"/></clipPath>
      <linearGradient id="panels-fade" x1="0" y1="0" x2="0" y2="1">
        <stop offset="0" stop-color="#f4f6f7"/><stop offset="1" stop-color="#e9ecee"/>
      </linearGradient>
      <linearGradient id="family-tone" x1="0" y1="0" x2="1" y2="1">
        <stop offset="0" stop-color="#bcdcf2"/><stop offset="0.5" stop-color="#b9a493"/><stop offset="1" stop-color="#d9d6cf"/>
      </linearGradient>
      <linearGradient id="installer-tone" x1="0" y1="0" x2="1" y2="1">
        <stop offset="0" stop-color="#c8e2f3"/><stop offset="0.5" stop-color="#d3a98a"/><stop offset="1" stop-color="#7d8796"/>
      </linearGradient>
      <linearGradient id="box-green" x1="0" y1="0" x2="1" y2="0">
        <stop offset="0" stop-color="var(--green)"/><stop offset="1" stop-color="var(--green-light)"/>
      </linearGradient>
    </defs>

    <rect class="panels-backdrop" role="img" aria-label="Faint photo of a house with rooftop solar panels" x="0" y="300" width="900" height="780" fill="url(#panels-fade)"/>

    <!-- top wave -->
    <path d="M0 395 Q200 290 440 325 L440 345 Q200 320 0 425 Z" fill="var(--blue)"/>
    <path d="M0 425 Q200 320 440 345 L440 420 L0 470 Z" fill="var(--green)"/>

    <!-- benefits box -->
    <path d="M43 400 Q240 330 430 340 L430 750 Q430 773 407 773 L66 773 Q43 773 43 750 Z" fill="url(#box-green)"/>
    <polygon points="140,380 463,380 463,422 430,422 430,455 430,422 140,422 150,401" fill="var(--blue)"/>
    <polygon points="430,422 463,422 430,455" fill="var(--blue-deep)"/>

    <!-- family photo -->
    <g clip-path="url(#family-clip)">
      <rect role="img" aria-label="Photo of a smiling family standing in front of a house with solar panels on the roof" x="400" y="0" width="500" height="510" fill="url(#family-tone)"/>
    </g>
    <path d="M462 0 Q395 110 402 230" stroke="var(--blue)" stroke-width="12" fill="none"/>
    <path d="M410 255 Q450 400 560 440" stroke="var(--green)" stroke-width="12" fill="none"/>
    <path d="M830 445 Q875 420 900 395" stroke="var(--green)" stroke-width="12" fill="none"/>

    <!-- installer photo -->
    <circle cx="675" cy="500" r="164" fill="var(--blue)"/>
    <g clip-path="url(#installer-clip)">
      <rect role="img" aria-label="Photo of a smiling installer in a hard hat working beside rooftop solar panels" x="515" y="340" width="320" height="320" fill="url(#installer-tone)"/>
    </g>

    <!-- bottom bands -->
    <path d="M0 1060 Q300 990 640 1060 L640 1090 Q300 1020 0 1095 Z" fill="var(--green)"/>
    <path d="M0 1095 Q300 1020 640 1090 L640 1273 L0 1273 Z" fill="var(--blue)"/>

    <!-- rebate seal -->
    <circle cx="760" cy="1140" r="160" fill="var(--white)"/>
    <path d="M690 1000 A150 150 0 0 0 660 1273" stroke="var(--green)" stroke-width="8" fill="none"/>
    <path d="M810 995 A150 150 0 0 1 900 1045" stroke="var(--blue)" stroke-width="8" fill="none"/>
  </svg>

  <h1 class="headline">GO<br>SOLAR</h1>

  <div class="easy-ribbon">WE MAKE IT EASY</div>
  <ul class="benefits">
    <li><b>$0 Down</b>, no upfront cost.</li>
    <li><b>Save 95%</b> off your utility bill.</li>
    <li>Protect yourself from rising energy costs.</li>
    <li>Provide clean, reliable energy for your family <b>powered by the sun</b>.</li>
  </ul>

  <div class="brand">
    <span class="brand-dot"></span>
    <div class="brand-name">BRIGHT ROOF ENERGY</div>
  </div>

  <h2 class="how-title">HOW IT WORKS...</h2>
  <p class="how-text">Your solar system allows you to <b>generate your own clean power</b> and COSTS LESS than your current utility company. Simply pay by the month, like you do now...but at a LOWER rate and <b>START SAVING IMMEDIATELY.</b></p>

  <div class="contact">
    <div class="contact-lead">Call Today For A No Obligation Consulting</div>
    <div class="contact-phone">555-014-7720</div>
    <div class="contact-web">www.brightroofenergy.com</div>
  </div>

  <div class="rebate">
    <div class="rebate-call">Call Today</div>
    <div class="rebate-receive">And Receive</div>
    <div class="rebate-amount">$500</div>
    <div class="rebate-label">Cash Rebate</div>
    <p class="rebate-terms">Limited time offer. Ad must be shown at time of purchase. Call for details. Not valid with any other offer or on previous purchases.</p>
  </div>
</main>
</body>
</html>
```